Business Cards for an 'affordable luxury' inner city home builder in Calgary.

We need a business card design that emulates the progressive, innovative, culture of our company and the modern style of our homes. Use our website www.velmarcrest-ab.com as a reference for the product we build.

Our company builds homes in the inner city space of Calgary, Alberta. We build affordable luxury.

Target Market(s)

Young professional Families

Contact Information for Business Card

Try to maintain consistency with the logo font and the card font.

Requirements
Must have
• The details must include: Name, education, title, phone number, website and email (Address is not as important)
• The design must be uniques (like our logo), elegant, sophisticated and modern.

```html
<!DOCTYPE html>
<html lang="en">
<head>
<meta charset="utf-8">
<title>Velmarcrest Homes Ltd — Business Card</title>
<link href="https://fonts.googleapis.com/css2?family=Montserrat:wght@500;600&family=Open+Sans:wght@400;700&display=swap" rel="stylesheet">
<style>
  :root {
    --backdrop: #94b02f;
    --card-dark: #000000;
    --card-light: #ffffff;
    --ink: #111111;
    --ink-soft: #2a2a2a;
    --rule: #3a3a3a;
    --mark-grey: #7d7d7d;
    --on-dark: #ffffff;
  }
  * { margin: 0; padding: 0; box-sizing: border-box; }
  html, body {
    width: 1200px;
    height: 1113px;
    overflow: hidden;
    background: var(--backdrop);
  }
  .canvas {
    position: relative;
    width: 1200px;
    height: 1113px;
  }
  .card {
    position: absolute;
    width: 600px;
    height: 343px;
    box-shadow: 0 6px 18px rgba(0, 0, 0, 0.18);
  }
  /* Front */
  .card-front {
    left: 150px;
    top: 150px;
    background: var(--card-dark);
    display: flex;
    align-items: center;
    justify-content: center;
  }
  .front-brand {
    display: flex;
    align-items: center;
    gap: 22px;
    color: var(--on-dark);
  }
  .brand-square {
    width: 60px;
    height: 60px;
    border: 3px solid var(--on-dark);
  }
  .front-name {
    font-family: "Montserrat", sans-serif;
    font-weight: 500;
    font-size: 24px;
    line-height: 1.1;
    letter-spacing: 1.5px;
    text-transform: uppercase;
  }
  /* Back */
  .card-back {
    left: 450px;
    top: 620px;
    background: var(--card-light);
    display: flex;
    align-items: center;
    padding: 0 40px 0 56px;
  }
  .back-brand {
    width: 200px;
    display: flex;
    flex-direction: column;
    align-items: flex-start;
    gap: 12px;
  }
  .back-square {
    width: 44px;
    height: 44px;
    background: var(--mark-grey);
  }
  .back-name {
    font-family: "Open Sans", sans-serif;
    font-weight: 700;
    font-size: 20px;
    letter-spacing: 1px;
    color: var(--ink);
    text-transform: uppercase;
    line-height: 1.15;
  }
  .divider {
    width: 1.5px;
    height: 124px;
    background: var(--rule);
    margin: 0 32px 0 20px;
  }
  .contact {
    font-family: "Open Sans", sans-serif;
    color: var(--ink);
  }
  .person-name {
    font-weight: 700;
    font-size: 19px;
    letter-spacing: 0.2px;
  }
  .person-title {
    font-weight: 700;
    font-size: 13px;
    margin-bottom: 18px;
    color: var(--ink-soft);
  }
  .contact-list { list-style: none; }
  .contact-item {
    display: flex;
    align-items: center;
    gap: 10px;
    font-size: 16px;
    line-height: 1.5;
  }
  .contact-icon {
    width: 13px;
    height: 13px;
    flex: none;
  }
</style>
</head>
<body>
<main class="canvas">
  <section class="card card-front" aria-label="Card front">
    <div class="front-brand">
      <span class="brand-square" aria-hidden="true"></span>
      <p class="front-name">Velmarcrest<br>Homes Ltd</p>
    </div>
  </section>

  <section class="card card-back" aria-label="Card back">
    <div class="back-brand">
      <span class="back-square" aria-hidden="true"></span>
      <p class="back-name">Velmarcrest<br>Homes</p>
    </div>
    <div class="divider" aria-hidden="true"></div>
    <div class="contact">
      <p class="person-name">SURNAME NAME Msc.</p>
      <p class="person-title">Founder &amp; CEO</p>
      <ul class="contact-list">
        <li class="contact-item">
          <svg class="contact-icon" viewBox="0 0 16 16" aria-hidden="true"><path fill="#111" d="M3.6 1.2l2.3 2.6-1.3 1.8c.9 2 2.5 3.7 4.6 4.7l1.8-1.3 2.7 2.2-1.3 2.6C7 13.6 2.3 8.9 1.1 2.6z"/></svg>
          <span>403-555-0148</span>
        </li>
        <li class="contact-item">
          <svg class="contact-icon" viewBox="0 0 16 16" aria-hidden="true"><rect x="1" y="3" width="14" height="10" fill="#111"/><path d="M1.5 3.5L8 9l6.5-5.5" stroke="#fff" stroke-width="1.3" fill="none"/></svg>
          <span>projects@velmarcrest-ab.com</span>
        </li>
        <li class="contact-item">
          <svg class="contact-icon" viewBox="0 0 16 16" aria-hidden="true"><g fill="none" stroke="#111" stroke-width="1.2"><circle cx="8" cy="8" r="6.5"/><ellipse cx="8" cy="8" rx="3" ry="6.5"/><path d="M1.5 8h13M2.5 4.8h11M2.5 11.2h11"/></g></svg>
          <span>www.velmarcrest-ab.com</span>
        </li>
      </ul>
    </div>
  </section>
</main>
</body>
</html>
```